Business Cards Needed for Innovative Healthcare Marketing Company

We are a marketing company focused on healthcare. Our company is all about rebranding yourself renewing your image and generating results. The phoenix stands for "reborn" or "rising" which we provide new brands for our clients we take their old brands and renew it with creativity and innovation. I am looking for a business card with color dimension. I have attached an example of a card I think has the look and feel of what I am trying to accomplish. I like that the card example has black and grey font colors, I like the font placement and the small logo, I really like the use of the colors on the right those are the colors of my logo. My logo is phoenix so maybe incorporating flames similar to that design. I would like the back a solid color maybe red with an opaque version of the logo and website. As a marketing company I am always open to creative liberty!

Target Market(s)

Doctors and business professionals.

Industry/Entity Type

Marketing

Contact Information for Business Card

Vornaly Health Care Marketing
Marnie Okonski- CEO
#(502)638-2947
email-marnie@vornaly.com
website- vornaly.com

Font styles to use
Sans Serif

Colors
ec1f27
f37122
ffc214
fbed22
fbf289
f04a50

Requirements
Must have
• The logo and required information
Nice to have
• icons by the information
Should not have
• child like font

```html
<!DOCTYPE html>
<html lang="en">
<head>
<meta charset="utf-8">
<title>Vornaly Health Care Marketing — Business Cards</title>
<link href="https://fonts.googleapis.com/css2?family=Raleway:wght@300&family=Roboto+Slab:wght@400;700&display=swap" rel="stylesheet">
<style>
  :root {
    --stage: #2b1c16;
    --maroon-deep: #3a0a0e;
    --maroon: #6e1a20;
    --maroon-light: #8a2026;
    --brick: #b0312a;
    --brick-dark: #7a1c1f;
    --white: #ffffff;
    --muted: #9aa7b4;
    --flame: #f37122;
    --flame-soft: #e0823c;
    --rose: #c4363b;
  }
  * { box-sizing: border-box; margin: 0; padding: 0; }
  html, body { width: 1200px; height: 913px; overflow: hidden; }
  body { background: var(--stage); position: relative; }

  .card {
    position: absolute;
    width: 560px;
    height: 330px;
    overflow: hidden;
    box-shadow: 0 18px 40px rgba(0,0,0,.45);
  }

  /* Back of card */
  .card-back {
    left: 70px; top: 70px;
    background: radial-gradient(ellipse at 62% 35%, var(--maroon-light) 0%, var(--maroon) 40%, var(--maroon-deep) 100%);
  }
  .card-back .brand {
    position: absolute;
    left: 250px; top: 112px;
    display: flex; align-items: center; gap: 14px;
  }
  .card-back .brand-dot {
    width: 40px; height: 40px; border-radius: 50%;
    background: rgba(20,8,8,.55);
  }
  .card-back .brand-name {
    font-family: "Raleway", sans-serif;
    font-weight: 300;
    font-size: 26px;
    line-height: 1.15;
    letter-spacing: 2px;
    color: var(--white);
    text-transform: uppercase;
  }
  .card-back .website {
    position: absolute;
    left: 300px; top: 222px;
    font-family: "Roboto Slab", serif;
    font-size: 20px;
    color: #d9d9d9;
    letter-spacing: .5px;
  }
  .card-back .website .domain { color: var(--rose); }

  /* Front of card */
  .card-front {
    left: 570px; top: 510px;
    background: var(--brick);
  }
  .card-front svg.panel { position: absolute; inset: 0; }
  .card-front .brand {
    position: absolute;
    left: 34px; top: 196px;
    display: flex; align-items: center; gap: 10px;
  }
  .card-front .brand-dot {
    width: 26px; height: 26px; border-radius: 50%;
    background: var(--flame);
  }
  .card-front .brand-name {
    font-family: "Raleway", sans-serif;
    font-weight: 300;
    font-size: 15px;
    line-height: 1.2;
    letter-spacing: 1.5px;
    color: var(--flame-soft);
    text-transform: uppercase;
  }
  .contact {
    position: absolute;
    left: 330px; top: 96px;
    font-family: "Roboto Slab", serif;
    color: var(--white);
  }
  .contact .name { font-size: 22px; font-weight: 700; }
  .contact .name .surname { text-transform: uppercase; }
  .contact .role { font-size: 15px; color: var(--muted); margin-top: 2px; }
  .contact ul { list-style: none; margin-top: 14px; }
  .contact li {
    display: flex; align-items: center; gap: 9px;
    font-size: 14px; margin-bottom: 7px;
  }
  .contact .icon {
    width: 20px; height: 20px; border-radius: 50%;
    background: var(--white);
    display: flex; align-items: center; justify-content: center;
  }
</style>
</head>
<body>

  <section class="card card-back" aria-label="Back of business card">
    <div class="brand">
      <span class="brand-dot"></span>
      <span class="brand-name">Vornaly<br>Health Care Marketing</span>
    </div>
    <p class="website">www.<span class="domain">vornaly</span>.com</p>
  </section>

  <section class="card card-front" aria-label="Front of business card">
    <svg class="panel" width="560" height="330" viewBox="0 0 560 330">
      <defs>
        <radialGradient id="panelShade" cx="35%" cy="45%" r="70%">
          <stop offset="0" stop-color="#5e1418"/>
          <stop offset="1" stop-color="#32090c"/>
        </radialGradient>
      </defs>
      <path d="M0 0 H220 C268 80 300 200 290 330 H0 Z" fill="url(#panelShade)"/>
      <path d="M238 0 H262 C300 90 318 200 306 330 H296 C306 210 286 100 238 0 Z" fill="var(--brick-dark)"/>
    </svg>

    <div class="brand">
      <span class="brand-dot"></span>
      <span class="brand-name">Vornaly<br>Health Care Marketing</span>
    </div>

    <div class="contact">
      <p class="name">Marnie <span class="surname">Okonski</span></p>
      <p class="role">CEO</p>
      <ul>
        <li>
          <span class="icon">
            <svg width="12" height="12" viewBox="0 0 24 24"><path fill="#7a1c1f" d="M6.6 10.8a15 15 0 0 0 6.6 6.6l2.2-2.2a1 1 0 0 1 1-.25 11.4 11.4 0 0 0 3.6.57 1 1 0 0 1 1 1V20a1 1 0 0 1-1 1A17 17 0 0 1 3 4a1 1 0 0 1 1-1h3.5a1 1 0 0 1 1 1c0 1.25.2 2.45.57 3.57a1 1 0 0 1-.25 1z"/></svg>
          </span>
          (502) 638-2947
        </li>
        <li>
          <span class="icon">
            <svg width="12" height="12" viewBox="0 0 24 24"><path fill="#7a1c1f" d="M3 5h18a1 1 0 0 1 1 1v12a1 1 0 0 1-1 1H3a1 1 0 0 1-1-1V6a1 1 0 0 1 1-1zm1 2.4V17h16V7.4l-8 5.3z M4.6 7 12 11.9 19.4 7z"/></svg>
          </span>
          marnie@vornaly.com
        </li>
      </ul>
    </div>
  </section>

</body>
</html>
```